How likely are people to engage in social distancing? We need a good illustration to show the data!

We surveyed U.S. adults March 20th - 24th, 2020 and asked how likely they were to engage in social distancing (and other COVID-19 related health behaviors). What did the survey find? Basically, most people intend to engage in social distancing behaviors (e.g., avoiding large crowds) and other behaviors that reduce the spread of COVID-19 (e.g., washing hands at least 20 seconds). When most people intend to engage in a behavior, then public health professionals try to leverage that to move more people to act.
Now we need innovative and professional images that attempt to communicate one or all of these findings. The specific findings are nicely summarized in the attached document. For example, 82% of participants intend to engage in social distancing.
What sort of visual are we looking for? Our preference is for an original illustration (or set of illustrations). Our preference is for (creative and powerful illustrations, but we are also open to the creative and well-executed infographics.
We need these images fast . We will award monetary prizes to the 3 best designs. If we like more than that, then we might purchase more (e.g., in past contests, we have purchased as many as 30 designs).
What we will need:
(1) The illustrations must be original and we will need the photoshop and/or illustrator files for all artwork.
(2) You can illustrate all of the findings or just one of them. We need creative approaches that do a lucid job of bringing the data to life. Most people intend to engage in these behaviors. How to communicate that? Corvantists and Halmerites do not differ in their intentions; how to communicate that?
(3) The illustration should say, somewhere: "Based on a survey of 400 U.S. adults conducted March 20 - 24th, 2020."

U.S. Adults

• Original illustrations based on the findings of the survey (see attached document).

```html
<!DOCTYPE html>
<html lang="en">
<head>
<meta charset="utf-8">
<title>Intended COVID-19 Health Behaviors</title>
<link rel="stylesheet" href="https://fonts.googleapis.com/css2?family=Bebas+Neue&family=Roboto+Condensed:wght@700&display=swap">
<style>
  :root {
    --bg: #f7f7f7;
    --teal: #2bbfae;
    --purple: #a56d9e;
    --yellow: #f9c74f;
    --sky: #4aa6c4;
    --mist: #9bbfcc;
    --green: #7fcf87;
    --blue: #2a7fc1;
    --orange: #f79a3e;
    --coral: #f27373;
    --brick: #a8302f;
    --white: #ffffff;
  }
  html, body {
    margin: 0;
    padding: 0;
    width: 1200px;
    height: 1000px;
    overflow: hidden;
    background: var(--bg);
  }
  .infographic { display: block; width: 1200px; height: 1000px; }
  .label {
    font-family: "Bebas Neue", "Oswald", sans-serif;
    font-size: 25px;
    text-anchor: middle;
  }
  .summary {
    font-family: "Bebas Neue", "Oswald", sans-serif;
    font-size: 36px;
    fill: var(--teal);
    text-anchor: middle;
  }
  .badge-value {
    font-family: "Roboto Condensed", "Arial Narrow", sans-serif;
    font-weight: 700;
    font-size: 15px;
    fill: var(--white);
    text-anchor: middle;
    dominant-baseline: central;
  }
  .hub-ring { fill: none; stroke: var(--teal); stroke-width: 4; }
  .badge-frame { fill: var(--white); stroke: var(--teal); stroke-width: 3; }
  .connector { stroke-width: 3; }
  .connector-dot { fill: var(--white); stroke-width: 3; }
  .topic-frame { fill: var(--white); stroke-width: 3; }
  .no-sign { fill: none; stroke-width: 11; }
</style>
</head>
<body>
<svg class="infographic" viewBox="0 0 1200 1000" xmlns="http://www.w3.org/2000/svg">
  <defs>
    <linearGradient id="g-purple" x1="0" y1="0" x2="1" y2="1"><stop offset="0" stop-color="#a56d9e"/><stop offset="1" stop-color="#4aa6a6"/></linearGradient>
    <linearGradient id="g-yellow" x1="0" y1="0" x2="1" y2="1"><stop offset="0" stop-color="#f9c74f"/><stop offset="1" stop-color="#5cc0a8"/></linearGradient>
    <linearGradient id="g-sky" x1="0" y1="0" x2="1" y2="1"><stop offset="0" stop-color="#4aa6c4"/><stop offset="1" stop-color="#2bbfae"/></linearGradient>
    <linearGradient id="g-mist" x1="0" y1="0" x2="1" y2="1"><stop offset="0" stop-color="#2bbfae"/><stop offset="1" stop-color="#9bbfcc"/></linearGradient>
    <linearGradient id="g-green" x1="0" y1="0" x2="1" y2="1"><stop offset="0" stop-color="#2bbfae"/><stop offset="1" stop-color="#7fcf87"/></linearGradient>
    <linearGradient id="g-blue" x1="0" y1="0" x2="1" y2="1"><stop offset="0" stop-color="#2bbfae"/><stop offset="1" stop-color="#2a7fc1"/></linearGradient>
    <linearGradient id="g-orange" x1="0" y1="0" x2="1" y2="1"><stop offset="0" stop-color="#f79a3e"/><stop offset="1" stop-color="#2bbfae"/></linearGradient>
    <linearGradient id="g-coral" x1="0" y1="0" x2="1" y2="1"><stop offset="0" stop-color="#f27373"/><stop offset="1" stop-color="#2bbfae"/></linearGradient>

    <radialGradient id="art-work"><stop offset="0" stop-color="#e9628f"/><stop offset="0.55" stop-color="#b07aa8"/><stop offset="1" stop-color="#f3e6f0"/></radialGradient>
    <radialGradient id="art-distancing"><stop offset="0" stop-color="#d9a53a"/><stop offset="0.55" stop-color="#e8c36a"/><stop offset="1" stop-color="#fbefd2"/></radialGradient>
    <radialGradient id="art-face"><stop offset="0" stop-color="#2f9fb0"/><stop offset="0.55" stop-color="#8ccbd9"/><stop offset="1" stop-color="#eaf5f8"/></radialGradient>
    <radialGradient id="art-wash"><stop offset="0" stop-color="#3d7a80"/><stop offset="0.55" stop-color="#93b9c4"/><stop offset="1" stop-color="#eef4f6"/></radialGradient>
    <radialGradient id="art-sanitizer"><stop offset="0" stop-color="#4fae4f"/><stop offset="0.55" stop-color="#9fd69f"/><stop offset="1" stop-color="#fbe4d6"/></radialGradient>
    <radialGradient id="art-space"><stop offset="0" stop-color="#2a5f8a"/><stop offset="0.55" stop-color="#7fb3dc"/><stop offset="1" stop-color="#e9f1f8"/></radialGradient>
    <radialGradient id="art-cancel"><stop offset="0" stop-color="#c0692a"/><stop offset="0.6" stop-color="#f0b27a"/><stop offset="1" stop-color="#fdeedd"/></radialGradient>
    <radialGradient id="art-gatherings"><stop offset="0" stop-color="#c45850"/><stop offset="0.6" stop-color="#eea7a0"/><stop offset="1" stop-color="#fbe9e7"/></radialGradient>
  </defs>

  <g class="connectors">
    <line class="connector" x1="597" y1="305" x2="597" y2="198" stroke="var(--purple)"/>
    <line class="connector" x1="733" y1="362" x2="808" y2="287" stroke="var(--yellow)"/>
    <line class="connector" x1="790" y1="498" x2="896" y2="498" stroke="var(--sky)"/>
    <line class="connector" x1="733" y1="636" x2="808" y2="712" stroke="var(--mist)"/>
    <line class="connector" x1="597" y1="690" x2="597" y2="801" stroke="var(--green)"/>
    <line class="connector" x1="462" y1="636" x2="384" y2="712" stroke="var(--blue)"/>
    <line class="connector" x1="405" y1="498" x2="294" y2="498" stroke="var(--orange)"/>
    <line class="connector" x1="462" y1="362" x2="382" y2="287" stroke="var(--coral)"/>
  </g>

  <circle class="hub-ring" cx="597" cy="497" r="193"/>
  <text class="summary" x="597" y="470">Based on a survey of</text>
  <text class="summary" x="597" y="512">400 U.S. adults conducted</text>
  <text class="summary" x="597" y="554">March 20 - 24th, 2020.</text>

  <g class="topic topic-work">
    <circle class="topic-frame" cx="597" cy="120" r="77" stroke="var(--purple)"/>
    <circle cx="597" cy="120" r="64" fill="url(#art-work)" role="img" aria-label="Illustration of a woman working on a laptop at a high table"/>
    <circle class="connector-dot" cx="597" cy="198" r="7" stroke="var(--purple)"/>
    <text class="label" x="597" y="39" fill="var(--purple)">Work from home</text>
  </g>
  <g class="topic topic-distancing">
    <circle class="topic-frame" cx="860" cy="236" r="77" stroke="var(--yellow)"/>
    <circle cx="860" cy="236" r="64" fill="url(#art-distancing)" role="img" aria-label="Illustration of a person sitting alone on a brick wall"/>
    <circle class="connector-dot" cx="808" cy="287" r="7" stroke="var(--yellow)"/>
    <text class="label" x="860" y="147" fill="var(--yellow)">Engage in social distancing</text>
  </g>
  <g class="topic topic-face">
    <circle class="topic-frame" cx="968" cy="498" r="75" stroke="var(--sky)"/>
    <circle cx="968" cy="498" r="62" fill="url(#art-face)" role="img" aria-label="Icon of a hand reaching toward a face, crossed out"/>
    <circle class="connector-dot" cx="896" cy="498" r="7" stroke="var(--sky)"/>
    <text class="label" x="968" y="383" fill="var(--sky)">Avoid touching your</text>
    <text class="label" x="968" y="413" fill="var(--sky)">eyes, nose, and mouth</text>
  </g>
  <g class="topic topic-wash">
    <circle class="topic-frame" cx="860" cy="765" r="77" stroke="var(--mist)"/>
    <circle cx="860" cy="765" r="64" fill="url(#art-wash)" role="img" aria-label="Illustration of a man washing his hands at a sink"/>
    <circle class="connector-dot" cx="808" cy="712" r="7" stroke="var(--mist)"/>
    <text class="label" x="860" y="869" fill="var(--mist)">Wash hands at</text>
    <text class="label" x="860" y="900" fill="var(--mist)">least 20 seconds</text>
  </g>
  <g class="topic topic-sanitizer">
    <circle class="topic-frame" cx="597" cy="878" r="77" stroke="var(--green)"/>
    <circle cx="597" cy="878" r="64" fill="url(#art-sanitizer)" role="img" aria-label="Illustration of a hand sanitizer bottle dispensing onto a hand"/>
    <circle class="connector-dot" cx="597" cy="801" r="7" stroke="var(--green)"/>
    <text class="label" x="597" y="979" fill="var(--green)">Use hand sanitizer</text>
  </g>
  <g class="topic topic-space">
    <circle class="topic-frame" cx="332" cy="765" r="77" stroke="var(--blue)"/>
    <circle cx="332" cy="765" r="64" fill="url(#art-space)" role="img" aria-label="Illustration of two masked people standing apart with virus particles between them"/>
    <circle class="connector-dot" cx="384" cy="712" r="7" stroke="var(--blue)"/>
    <text class="label" x="332" y="869" fill="var(--blue)">Put distance between</text>
    <text class="label" x="332" y="900" fill="var(--blue)">yourself and other people</text>
  </g>
  <g class="topic topic-cancel">
    <circle class="topic-frame" cx="220" cy="498" r="75" stroke="var(--orange)"/>
    <circle cx="220" cy="498" r="62" fill="url(#art-cancel)" role="img" aria-label="Illustration of a small group of people behind a prohibition sign"/>
    <g class="no-sign" stroke="var(--orange)">
      <circle cx="220" cy="498" r="52"/>
      <line x1="184" y1="462" x2="256" y2="534"/>
    </g>
    <circle class="connector-dot" cx="294" cy="498" r="7" stroke="var(--orange)"/>
    <text class="label" x="220" y="412" fill="var(--orange)">Cancel social activities</text>
  </g>
  <g class="topic topic-gatherings">
    <circle class="topic-frame" cx="330" cy="235" r="77" stroke="var(--coral)"/>
    <circle cx="330" cy="235" r="64" fill="url(#art-gatherings)" role="img" aria-label="Illustration of a group of people behind a prohibition sign"/>
    <g class="no-sign" stroke="var(--brick)">
      <circle cx="330" cy="235" r="52"/>
      <line x1="294" y1="199" x2="366" y2="271"/>
    </g>
    <circle class="connector-dot" cx="382" cy="287" r="7" stroke="var(--coral)"/>
    <text class="label" x="330" y="147" fill="var(--coral)">Avoid large gatherings</text>
  </g>

  <g class="badges">
    <circle class="badge-frame" cx="597" cy="305" r="26"/><circle cx="597" cy="305" r="20" fill="url(#g-purple)"/><text class="badge-value" x="597" y="305">63%</text>
    <circle class="badge-frame" cx="733" cy="362" r="26"/><circle cx="733" cy="362" r="20" fill="url(#g-yellow)"/><text class="badge-value" x="733" y="362">82%</text>
    <circle class="badge-frame" cx="790" cy="498" r="26"/><circle cx="790" cy="498" r="20" fill="url(#g-sky)"/><text class="badge-value" x="790" y="498">81%</text>
    <circle class="badge-frame" cx="733" cy="636" r="26"/><circle cx="733" cy="636" r="20" fill="url(#g-mist)"/><text class="badge-value" x="733" y="636">87%</text>
    <circle class="badge-frame" cx="597" cy="690" r="26"/><circle cx="597" cy="690" r="20" fill="url(#g-green)"/><text class="badge-value" x="597" y="690">85%</text>
    <circle class="badge-frame" cx="462" cy="636" r="26"/><circle cx="462" cy="636" r="20" fill="url(#g-blue)"/><text class="badge-value" x="462" y="636">85%</text>
    <circle class="badge-frame" cx="405" cy="498" r="26"/><circle cx="405" cy="498" r="20" fill="url(#g-orange)"/><text class="badge-value" x="405" y="498">81%</text>
    <circle class="badge-frame" cx="462" cy="362" r="26"/><circle cx="462" cy="362" r="20" fill="url(#g-coral)"/><text class="badge-value" x="462" y="362">85%</text>
  </g>
</svg>
</body>
</html>
```